Natural Skin Care e commerce website

we are the distributor for natural skincare product , we would like to develop a e commerce website which encompass the ability to divide the product into face, body , baby , and base on ingredient , best seller, we are Olvexa certified product the key point to focus is natural organic , no nasties, vegan , unpolluted , full of natural ingredient. manuka, olive nordic style temporary style website is preferred. the website name is Quillom store.co , the web must have ability to take the order and let the brand upload their products

```html
<!DOCTYPE html>
<html lang="en">
<head>
<meta charset="utf-8">
<title>Quillom Store – Natural Skin Care</title>
<link rel="stylesheet" href="https://fonts.googleapis.com/css2?family=Poppins:ital,wght@0,400;0,500;0,600;1,400&family=Rufina:wght@700&display=swap">
<style>
:root{
  --teal:#109a8b;
  --teal-dark:#0b3c40;
  --ink:#1d2b2d;
  --muted:#666f70;
  --mint:#e5f2f0;
  --mint-2:#cfe8e4;
  --grey-bg:#f5f5f5;
  --white:#ffffff;
}
*{box-sizing:border-box;margin:0;padding:0}
html,body{width:1200px;height:4536px;overflow:hidden}
body{position:relative;background:var(--white);font-family:'Poppins',sans-serif;color:var(--ink)}
.abs{position:absolute}
.accent{color:var(--teal)}
.section-title{position:absolute;left:0;width:1200px;text-align:center;font-size:42px;font-weight:500;letter-spacing:.5px}
.section-sub{position:absolute;left:0;width:1200px;text-align:center;font-size:14.5px;line-height:25px;color:var(--muted)}
.ph{position:absolute}

/* top bar + nav */
.topbar{left:0;top:0;width:1200px;height:40px;background:var(--teal-dark);color:#fff;font-size:14px;text-align:center;line-height:40px}
.topbar span{color:#19c2ad}
.nav{left:0;top:40px;width:1200px;height:84px;background:#fff}
.brand{font-weight:600;color:var(--teal);font-size:22px;letter-spacing:.3px}
.nav .brand{left:79px;top:28px}
.menu{left:490px;top:30px;display:flex;gap:26px;font-size:15px}
.menu .on{color:var(--teal)}
.nav-icons{left:1018px;top:28px;display:flex;gap:14px}

/* hero */
.hero{left:0;top:124px;width:1200px;height:566px;overflow:hidden}
.hero-title{left:78px;top:134px;font-family:'Rufina',serif;font-size:62px;line-height:66px;color:var(--teal-dark)}
.hero-title .accent{color:var(--teal)}
.hero-text{left:80px;top:278px;font-size:16px;line-height:27px;width:360px}
.btn{display:inline-block;background:var(--teal);color:#fff;border-radius:30px;font-weight:500;text-align:center;text-transform:uppercase}
.hero .btn{left:76px;top:348px;width:228px;height:56px;line-height:56px;font-size:18px}
.arrow-btn{width:52px;height:52px;border-radius:50%;display:flex;align-items:center;justify-content:center}

/* products */
.product{position:absolute;top:902px;width:245px}
.product .shot{width:245px;height:270px;background:linear-gradient(#f3f3f3,#ececec)}
.badge-new{position:absolute;left:16px;top:14px;background:var(--teal-dark);color:#fff;font-size:13px;font-weight:600;padding:2px 9px}
.product h4{font-size:18.5px;font-weight:500;margin-top:22px;white-space:nowrap}
.stars{margin-top:6px;display:flex;gap:3px}
.price{font-size:18px;font-weight:600;margin-top:6px}

/* category */
.cat-band{left:0;top:1827px;width:1200px;height:323px;background:var(--mint)}
.cat{position:absolute;top:1526px;width:312px;height:365px}
.cat span{position:absolute;left:0;bottom:22px;width:100%;text-align:center;color:#fff;font-size:21px;font-weight:500}
.feature{position:absolute;top:1955px;width:200px;text-align:center;font-size:19px}
.feature svg{display:block;margin:0 auto 16px}

/* certified */
.cert-title{left:177px;top:2258px;font-size:42px;font-weight:500;line-height:52px}
.cert-text{left:347px;top:2402px;width:260px;font-size:14.5px;line-height:25px;color:var(--muted)}

/* testimonials */
.happy{left:0;top:2705px;width:1200px;height:930px}
.client{position:absolute;top:2869px;width:340px}
.avatar{position:absolute;left:0;top:0;width:84px;height:84px;border-radius:50%}
.client h5{position:absolute;left:104px;top:22px;font-size:19px;font-weight:500;white-space:nowrap}
.client .site{position:absolute;left:104px;top:50px;font-size:15px;color:var(--teal)}
.client p{position:absolute;left:108px;top:86px;width:240px;font-size:14.5px;line-height:27px;font-style:italic;color:var(--muted)}
.divider{left:78px;top:3094px;width:1044px;height:1px;background:#dcdcdc}

/* blog */
.blog-title{left:79px;top:3265px;font-size:42px;font-weight:500}
.blog-text{left:79px;top:3326px;width:280px;font-size:15px;line-height:27px;color:var(--muted)}
.visit{left:79px;top:3397px;font-size:14.5px;font-weight:600;color:var(--teal);display:flex;align-items:center;gap:14px}
.card{position:absolute;top:3163px;width:301px;height:394px;background:#fff}
.card .img{height:218px}
.card .date{position:absolute;left:24px;top:242px;font-size:14px;color:var(--teal)}
.card h6{position:absolute;left:22px;top:272px;width:260px;font-size:17px;font-weight:500;line-height:28px}
.card svg{position:absolute;left:24px;top:350px}

/* newsletter */
.news-title{left:573px;top:3758px;font-size:38px;font-weight:500}
.news-sub{left:573px;top:3812px;font-size:14.5px;color:var(--muted)}
.field{position:absolute;left:571px;width:458px;height:54px;border:1px solid #e2e2e2;border-radius:28px;font-size:14.5px;color:var(--muted);padding-left:26px;line-height:52px;background:#fff}
.subscribe{left:571px;top:3989px;width:176px;height:56px;line-height:56px;font-size:19px}

/* footer */
.foot-col{position:absolute;top:4212px}
.foot-col h3{font-size:17px;font-weight:500;margin-bottom:14px}
.foot-col li{list-style:none;font-size:14.5px;line-height:29px;display:flex;align-items:center;gap:14px}
.foot-col li::before{content:"";width:6px;height:6px;border:2px solid var(--teal);border-radius:50%}
.contact{position:absolute;left:870px;display:flex;align-items:center;gap:18px;font-size:14.5px}
.social{position:absolute;top:4359px;width:46px;height:46px;border:2px solid var(--teal);border-radius:50%}
.copy{left:0;top:4488px;width:1200px;text-align:center;font-size:14.5px;color:var(--muted)}
</style>
</head>
<body>

<!-- header -->
<div class="abs topbar">Quillom Store - <span>Free Delivery Products</span></div>
<header class="abs nav">
  <div class="abs brand">QUILLOM STORE</div>
  <nav class="abs menu"><span class="on">Home</span><span>Products</span><span>Go Natural</span><span>About</span><span>Blog</span><span>Contact</span></nav>
  <div class="abs nav-icons">
    <svg width="24" height="24" viewBox="0 0 24 24"><path d="M2 5h3l3 11h11l2-8H7" fill="none" stroke="#0b3c40" stroke-width="2.4"/><circle cx="9" cy="20" r="1.8" fill="#0b3c40"/><circle cx="17" cy="20" r="1.8" fill="#0b3c40"/><circle cx="19" cy="5" r="5" fill="#109a8b"/></svg>
    <svg width="22" height="22" viewBox="0 0 22 22"><circle cx="11" cy="6" r="5" fill="#0b3c40"/><path d="M2 21c0-6 4-8 9-8s9 2 9 8z" fill="#0b3c40"/></svg>
    <svg width="24" height="22" viewBox="0 0 24 22"><path d="M12 21 2 11a5.5 5.5 0 0 1 10-6 5.5 5.5 0 0 1 10 6z" fill="#0b3c40"/></svg>
  </div>
</header>

<!-- hero -->
<section class="abs hero">
  <svg class="abs" style="left:0;top:0" width="1200" height="566" viewBox="0 0 1200 566">
    <path d="M0 0h1200v450C900 560 300 560 0 515z" fill="#e8f3f2"/>
    <path d="M0 0h320c20 150-40 240-180 250C70 255 20 230 0 210z" fill="#cfe9e5"/>
  </svg>
  <div class="ph" role="img" aria-label="Model with leaf over her face and two skincare bottles" style="left:530px;top:0;width:670px;height:566px;background:linear-gradient(120deg,#dfe7e3 0%,#cfd6cf 25%,#e5c9b5 55%,#d8b59d 80%,#e8f3f2 100%);clip-path:polygon(0 0,100% 0,100% 80%,60% 95%,0 100%)"></div>
  <h1 class="abs hero-title">NATURAL<br><span class="accent">SKIN CARE</span></h1>
  <p class="abs hero-text">Lorem Ipsum is simply dummy text of the printing and typesetting industry.</p>
  <span class="abs btn">View Products</span>
  <div class="ph" role="img" aria-label="Olive sprig decoration" style="left:210px;top:376px;width:215px;height:110px;background:radial-gradient(ellipse at center,#8fb25e 0%,rgba(143,178,94,.35) 45%,rgba(143,178,94,0) 70%)"></div>
  <div class="abs arrow-btn" style="left:13px;top:236px;background:#fff"><svg width="16" height="16" viewBox="0 0 16 16"><path d="M10 2 4 8l6 6" fill="none" stroke="#0b3c40" stroke-width="2"/></svg></div>
  <div class="abs arrow-btn" style="left:1137px;top:236px;background:var(--teal)"><svg width="16" height="16" viewBox="0 0 16 16"><path d="M6 2l6 6-6 6" fill="none" stroke="#fff" stroke-width="2"/></svg></div>
</section>

<!-- best seller -->
<h2 class="section-title" style="top:748px">BEST <span class="accent">SELLER</span></h2>
<p class="section-sub" style="top:812px">Lorem Ipsum is simply dummy text of the printing and typesetting<br>industry Lorem Ipsum has been the industry</p>

<div class="product" style="left:77px"><div class="ph shot" role="img" aria-label="Clear toner bottle" style="position:relative"></div><h4>Product Name Quillom</h4><div class="stars"><svg width="100" height="16" viewBox="0 0 100 16"><g fill="#109a8b"><path id="st" d="M8 0l2.4 5 5.6.6-4.2 3.8 1.2 5.6L8 12.2 3 15l1.2-5.6L0 5.6 5.6 5z"/><use href="#st" x="20"/><use href="#st" x="40"/><use href="#st" x="60"/><use href="#st" x="80"/></g></svg></div><div class="price">$34</div></div>
<div class="product" style="left:341px"><div class="ph shot" role="img" aria-label="White serum bottle" style="position:relative"><span class="badge-new">NEW</span></div><h4>Product Name Quillom</h4><div class="stars"><svg width="100" height="16" viewBox="0 0 100 16"><g fill="#109a8b"><use href="#st"/><use href="#st" x="20"/><use href="#st" x="40"/><use href="#st" x="60"/><use href="#st" x="80"/></g></svg></div><div class="price">$34</div></div>
<div class="product" style="left:607px"><div class="ph shot" role="img" aria-label="Pale green pump bottle" style="position:relative"></div><h4>Product Name Quillom</h4><div class="stars"><svg width="100" height="16" viewBox="0 0 100 16"><g fill="#109a8b"><use href="#st"/><use href="#st" x="20"/><use href="#st" x="40"/><use href="#st" x="60"/><use href="#st" x="80"/></g></svg></div><div class="price">$34</div></div>
<div class="product" style="left:873px"><div class="ph shot" role="img" aria-label="White serum bottle" style="position:relative"></div><h4>Product Name Quillom</h4><div class="stars"><svg width="100" height="16" viewBox="0 0 100 16"><g fill="#109a8b"><use href="#st"/><use href="#st" x="20"/><use href="#st" x="40"/><use href="#st" x="60"/><use href="#st" x="80"/></g></svg></div><div class="price">$34</div></div>

<!-- category -->
<div class="abs cat-band"></div>
<h2 class="section-title" style="top:1377px">OUR <span class="accent">CATEGORY</span></h2>
<p class="section-sub" style="top:1441px">Lorem Ipsum is simply dummy text of the printing and typesetting<br>industry Lorem Ipsum has been the industry</p>
<div class="cat" role="img" aria-label="Face care category photo" style="left:128px;background:linear-gradient(#c7cdcf 0%,#8a6f5e 45%,#1c4e50 100%)"><span>FACE</span></div>
<div class="cat" role="img" aria-label="Baby care category photo" style="left:443px;background:linear-gradient(#9aa0a2 0%,#c6a48e 45%,#1c4e50 100%)"><span>BABY</span></div>
<div class="cat" role="img" aria-label="Body care category photo" style="left:758px;background:linear-gradient(#d9c8a2 0%,#c89c8a 45%,#1c4e50 100%)"><span>BODY</span></div>

<div class="feature" style="left:125px"><svg width="72" height="66" viewBox="0 0 72 66" fill="none" stroke="#0b3c40" stroke-width="2.2"><path d="M14 56 52 14"/><path d="M36 32c-6-10-4-22 2-28 6 8 6 20-2 28z" fill="#109a8b"/><path d="M42 34c8-6 20-6 26 0-8 6-18 6-26 0z" fill="#109a8b"/><ellipse cx="24" cy="44" rx="8" ry="6"/><ellipse cx="34" cy="52" rx="8" ry="6"/></svg>Natural Organic</div>
<div class="feature" style="left:324px"><svg width="72" height="66" viewBox="0 0 72 66" fill="none" stroke="#0b3c40" stroke-width="2.2"><circle cx="36" cy="33" r="28"/><path d="M16 53 56 13" stroke="#109a8b" stroke-width="3"/><path d="M28 22v24M40 22v24M28 34h12"/></svg>No Nasties</div>
<div class="feature" style="left:500px"><svg width="72" height="66" viewBox="0 0 72 66" fill="none" stroke="#0b3c40" stroke-width="2.2"><path d="M12 26c0-12 10-20 22-20s22 8 22 20z"/><path d="M28 26v28h12V26"/><path d="M40 40c6-4 14-2 18 4-6 4-14 2-18-4z" fill="#109a8b"/></svg>vegan</div>
<div class="feature" style="left:669px"><svg width="72" height="66" viewBox="0 0 72 66" fill="none" stroke="#0b3c40" stroke-width="2.2"><path d="M36 4c10 10 10 26 0 34-10-8-10-24 0-34z" fill="#109a8b"/><path d="M36 38v12"/><path d="M8 34l10 16h14M64 34 54 50H40"/></svg>Unpolluted</div>
<div class="feature" style="left:885px"><svg width="72" height="66" viewBox="0 0 72 66" fill="none" stroke="#0b3c40" stroke-width="2.2"><path d="M10 36h44c0 12-10 20-22 20S10 48 10 36z"/><path d="M26 36c-10-8-10-20-2-28 8 8 8 20 2 28z" fill="#109a8b"/><path d="M32 36c6-10 16-12 24-6-6 6-16 8-24 6z" fill="#109a8b"/><path d="M50 22 66 6"/></svg>Natural Ingredient</div>

<!-- certified -->
<h2 class="abs cert-title">OLVEXA CERTIFIED<br><span class="accent">PRODUCTS</span></h2>
<svg class="abs" style="left:176px;top:2389px" width="144" height="144" viewBox="0 0 144 144"><circle cx="72" cy="72" r="68" fill="#fff" stroke="#6b6b6b" stroke-width="7"/><circle cx="72" cy="72" r="48" fill="#6b6b6b"/></svg>
<p class="abs cert-text">Lorem Ipsum is simply dummy text of the printing and typesetting industry Lorem Ipsum has been the industry</p>
<span class="abs btn" style="left:331px;top:2523px;width:229px;height:57px;line-height:57px;font-size:18px">View Products</span>
<div class="ph" role="img" aria-label="Natural oils, salts and loofah on a table" style="left:661px;top:2215px;width:301px;height:299px;background:linear-gradient(135deg,#d9cbb0,#b08b5e 50%,#6e5a44)"></div>
<div class="ph" role="img" aria-label="Olive sprig decoration" style="left:965px;top:2285px;width:128px;height:90px;background:radial-gradient(ellipse,#7ea454 0%,rgba(126,164,84,0) 70%)"></div>
<div class="ph" role="img" aria-label="Model holding a green leaf" style="left:800px;top:2382px;width:240px;height:240px;background:linear-gradient(120deg,#2f5a34,#c9997c 55%,#3f6b3d)"></div>

<!-- testimonials -->
<svg class="abs happy" viewBox="0 0 1200 930"><path d="M0 40C300 -10 900 -10 1200 40V930H0z" fill="#f5f5f5"/></svg>
<h2 class="section-title" style="top:2769px">HAPPY <span class="accent">EXPERIENCE</span></h2>
<div class="client" style="left:76px"><div class="avatar" role="img" aria-label="Client portrait" style="background:linear-gradient(#e9cf9d,#c99a72)"></div><h5>Client Name</h5><span class="site">something.com</span><p>"Lorem Ipsum is simply text of the printing and typesetting is industry Lorem Ipsumy "</p></div>
<div class="client" style="left:432px"><div class="avatar" role="img" aria-label="Client portrait" style="background:linear-gradient(#3a2a24,#c08a6c)"></div><h5>Client Name</h5><span class="site">something.com</span><p>"Lorem Ipsum is simply text of the printing and typesetting is industry Lorem Ipsumy "</p></div>
<div class="client" style="left:790px"><div class="avatar" role="img" aria-label="Client portrait" style="background:linear-gradient(#4a3a2a,#b7876a)"></div><h5>Client Name</h5><span class="site">something.com</span><p>"Lorem Ipsum is simply text of the printing and typesetting is industry Lorem Ipsumy "</p></div>
<div class="abs divider"></div>

<!-- blog -->
<h2 class="abs blog-title">THE <span class="accent">BLOG</span></h2>
<p class="abs blog-text">Lorem Ipsum is simply text of the printing and typesetting.</p>
<div class="abs visit">Visit Blog <svg width="28" height="10" viewBox="0 0 28 10"><path d="M0 5h26M21 1l5 4-5 4" fill="none" stroke="#0b3c40" stroke-width="1.8"/></svg></div>
<div class="abs arrow-btn" style="left:295px;top:3477px;background:#fff"><svg width="14" height="14" viewBox="0 0 16 16"><path d="M10 2 4 8l6 6" fill="none" stroke="#109a8b" stroke-width="2"/></svg></div>
<div class="abs arrow-btn" style="left:356px;top:3477px;background:var(--teal)"><svg width="14" height="14" viewBox="0 0 16 16"><path d="M6 2l6 6-6 6" fill="none" stroke="#fff" stroke-width="2"/></svg></div>

<article class="card" style="left:435px"><div class="img" role="img" aria-label="Herbal tea and oil bottles" style="background:linear-gradient(135deg,#3d3a2c,#8a6a3c 55%,#2a2a22)"></div><span class="date">15 MAY 2020</span><h6>Lorem Ipsum is Simply Text of The Printing</h6><svg width="28" height="10" viewBox="0 0 28 10"><path d="M0 5h26M21 1l5 4-5 4" fill="none" stroke="#109a8b" stroke-width="1.8"/></svg></article>
<article class="card" style="left:768px"><div class="img" role="img" aria-label="Coconut cream among palm leaves" style="background:linear-gradient(135deg,#2f6f5c,#7fb3c4 50%,#dfe9ec)"></div><span class="date">15 MAY 2020</span><h6>Lorem Ipsum is Simply Text of The Printing</h6><svg width="28" height="10" viewBox="0 0 28 10"><path d="M0 5h26M21 1l5 4-5 4" fill="none" stroke="#109a8b" stroke-width="1.8"/></svg></article>
<article class="card" style="left:1101px"><div class="img" role="img" aria-label="Spa candles and wooden tray" style="background:linear-gradient(135deg,#6a5a3a,#c9b28a)"></div><span class="date">15 MAY 2020</span><h6>Lorem Ipsum is Simply Text of The Printing</h6><svg width="28" height="10" viewBox="0 0 28 10"><path d="M0 5h26M21 1l5 4-5 4" fill="none" stroke="#109a8b" stroke-width="1.8"/></svg></article>

<!-- newsletter -->
<svg class="abs" style="left:0;top:4100px" width="1200" height="436" viewBox="0 0 1200 436"><path d="M0 40C400 0 800 0 1200 40V436H0z" fill="#f5f5f5"/></svg>
<div class="ph" style="left:70px;top:3797px;width:406px;height:406px;border-radius:50%;background:var(--teal)"></div>
<div class="ph" role="img" aria-label="Group of white and green skincare jars and bottles" style="left:160px;top:3700px;width:340px;height:440px;background:linear-gradient(#f4f4f2,#dfe5e2 60%,#4f8e74);border-radius:16px 16px 0 0"></div>
<h2 class="abs news-title">NEWSLETTER <span class="accent">SIGNUP!</span></h2>
<p class="abs news-sub">Would you like to Receive our exclusive update for Sigh up</p>
<div class="field" style="top:3853px">Enter Name *</div>
<div class="field" style="top:3921px">Enter Email *</div>
<span class="abs btn subscribe">Subscribe</span>
<div class="ph" role="img" aria-label="Olive sprig decoration" style="left:995px;top:4050px;width:205px;height:120px;background:radial-gradient(ellipse,#7ea454 0%,rgba(126,164,84,0) 70%)"></div>

<!-- footer -->
<div class="foot-col" style="left:78px"><h3>SITE <span class="accent">MAP</span></h3><ul><li>Home</li><li>Products</li><li>Go Natural</li><li>About</li><li>Blog</li><li>Contact</li></ul></div>
<div class="foot-col" style="left:344px"><h3>SHOP <span class="accent">NOW</span></h3><ul><li>Face</li><li>Body</li><li>Baby</li><li>Best Seller</li></ul></div>
<div class="foot-col" style="left:610px"><h3>QUICK <span class="accent">LINKS</span></h3><ul><li>privacy policy</li><li>Terms &amp; conditions</li><li>Booking policy</li><li>Reaturn Policy</li><li>100% Gurantee</li><li>Help</li></ul></div>
<div class="abs brand" style="left:870px;top:4220px">QUILLOM STORE</div>
<div class="contact" style="top:4272px"><svg width="22" height="22" viewBox="0 0 22 22"><path d="M5 2l4 4-2 3c1 3 3 5 6 6l3-2 4 4-3 3C9 20 2 13 2 5z" fill="none" stroke="#109a8b" stroke-width="1.8"/></svg>123 555 0190</div>
<div class="contact" style="top:4310px"><svg width="22" height="16" viewBox="0 0 22 16"><rect x="1" y="1" width="20" height="14" fill="#109a8b"/><path d="M1 1l10 8 10-8" fill="none" stroke="#fff" stroke-width="1.6"/></svg>info@quillomstore.co</div>
<div class="social" style="left:870px"></div>
<div class="social" style="left:925px"></div>
<div class="social" style="left:980px"></div>
<p class="abs copy">©Quillom <span class="accent">Store</span> - 2020 All rights reserved.</p>

</body>
</html>
```